Darlene Whitcott

I need all of my logos on one card. I would like a burgundy back and Harbor Shield and Tamsworth insurance being the most prominent.
Phone Number 541-382-9154
Web:
www.Tamsworthins.example
www.Harbor Shield.example
www.Kell-Insurance.example

```html
<!DOCTYPE html>
<html lang="en">
<head>
<meta charset="utf-8">
<title>Harbor Shield – Business Card</title>
<link href="https://fonts.googleapis.com/css2?family=Cinzel:wght@500&family=Montserrat:wght@400&display=swap" rel="stylesheet">
<style>
  :root {
    --bg: #4a4c50;
    --burgundy: #6e1a2c;
    --gold: #bea236;
    --ink: #1a1a1a;
    --paper: #ffffff;
  }
  html, body {
    margin: 0;
    padding: 0;
    width: 1200px;
    height: 960px;
    overflow: hidden;
    background: var(--bg);
  }
  .canvas {
    position: relative;
    width: 1200px;
    height: 960px;
  }
  .card {
    position: absolute;
    width: 560px;
    height: 320px;
    border-radius: 30px;
    box-shadow: 0 18px 40px rgba(0,0,0,0.45);
    overflow: hidden;
  }
  .card-back {
    left: 70px;
    top: 110px;
    background: var(--burgundy);
    display: flex;
    flex-direction: column;
    align-items: center;
    justify-content: center;
    gap: 10px;
  }
  .card-front {
    left: 570px;
    top: 510px;
    background: var(--paper);
  }
  .brand-name,
  .agency-name {
    font-family: "Cinzel", serif;
    font-weight: 500;
    margin: 0;
    white-space: nowrap;
  }
  .card-back .brand-name {
    font-size: 46px;
    letter-spacing: 2px;
    color: var(--paper);
  }
  .card-back .agency-name {
    font-size: 24px;
    letter-spacing: 3px;
    color: var(--gold);
  }
  .card-front .brand-name {
    position: absolute;
    right: 36px;
    top: 30px;
    font-size: 36px;
    letter-spacing: 2px;
    color: var(--gold);
  }
  .card-front .agency-name {
    position: absolute;
    right: 36px;
    top: 80px;
    font-size: 19px;
    letter-spacing: 3px;
    color: var(--ink);
  }
  .person-name {
    position: absolute;
    left: 36px;
    top: 124px;
    margin: 0;
    font-family: "Cinzel", serif;
    font-weight: 500;
    font-size: 28px;
    line-height: 34px;
    color: var(--gold);
  }
  .divider {
    position: absolute;
    left: 36px;
    right: 34px;
    top: 162px;
    height: 3px;
    background: var(--ink);
  }
  .person-title {
    position: absolute;
    left: 40px;
    top: 172px;
    margin: 0;
    font-family: "Montserrat", sans-serif;
    font-size: 19px;
    line-height: 24px;
    color: var(--ink);
  }
  .phone {
    position: absolute;
    right: 36px;
    top: 174px;
    display: flex;
    align-items: center;
    gap: 8px;
    font-family: "Montserrat", sans-serif;
    font-size: 18px;
    line-height: 24px;
    color: var(--ink);
  }
  .web-list {
    position: absolute;
    left: 44px;
    top: 214px;
    margin: 0;
    padding: 0;
    list-style: none;
    font-family: "Montserrat", sans-serif;
    font-size: 18px;
    color: var(--ink);
  }
  .web-list li {
    display: flex;
    align-items: center;
    gap: 12px;
    height: 28px;
  }
  .icon { flex: none; }
</style>
</head>
<body>
<div class="canvas">
  <section class="card card-back">
    <h2 class="brand-name">HARBOR SHIELD</h2>
    <p class="agency-name">TAMSWORTH INSURANCE</p>
  </section>

  <section class="card card-front">
    <h2 class="brand-name">HARBOR SHIELD</h2>
    <p class="agency-name">TAMSWORTH INSURANCE</p>
    <h1 class="person-name">YOUR NAME</h1>
    <div class="divider"></div>
    <p class="person-title">YOUR TITLE</p>

    <div class="phone">
      <svg class="icon" width="16" height="16" viewBox="0 0 24 24" aria-hidden="true">
        <path fill="#bea236" d="M6.6 10.8c1.4 2.8 3.8 5.1 6.6 6.6l2.2-2.2c.3-.3.7-.4 1-.2 1.1.4 2.3.6 3.6.6.6 0 1 .4 1 1V20c0 .6-.4 1-1 1C10.6 21 3 13.4 3 4c0-.6.4-1 1-1h3.5c.6 0 1 .4 1 1 0 1.3.2 2.5.6 3.6.1.3 0 .7-.2 1z"/>
      </svg>
      <span>541-382-9154</span>
    </div>

    <ul class="web-list">
      <li>
        <svg class="icon" width="20" height="20" viewBox="0 0 20 20" aria-hidden="true">
          <circle cx="10" cy="10" r="8" fill="none" stroke="#bea236" stroke-width="2.5"/>
          <path d="M2 10h16M10 2c3 3 3 13 0 16M10 2c-3 3-3 13 0 16" fill="none" stroke="#bea236" stroke-width="1.5"/>
        </svg>
        <span>www.Tamsworthins.example</span>
      </li>
      <li>
        <svg class="icon" width="20" height="20" viewBox="0 0 20 20" aria-hidden="true">
          <circle cx="10" cy="10" r="8" fill="none" stroke="#bea236" stroke-width="2.5"/>
          <path d="M2 10h16M10 2c3 3 3 13 0 16M10 2c-3 3-3 13 0 16" fill="none" stroke="#bea236" stroke-width="1.5"/>
        </svg>
        <span>www.Harbor Shield.example</span>
      </li>
      <li>
        <svg class="icon" width="20" height="20" viewBox="0 0 20 20" aria-hidden="true">
          <circle cx="10" cy="10" r="8" fill="none" stroke="#bea236" stroke-width="2.5"/>
          <path d="M2 10h16M10 2c3 3 3 13 0 16M10 2c-3 3-3 13 0 16" fill="none" stroke="#bea236" stroke-width="1.5"/>
        </svg>
        <span>www.Kell-Insurance.example</span>
      </li>
    </ul>
  </section>
</div>
</body>
</html>
```